BRINEWAKE DIVE

IM LOOKING AT A BROCHURE MY MY DIVE CENTRE WE DO COURSES FROM INTRO TO PROFESSIONAL, IM OPEN TO DESIGN AND COLOURS, JUST LOOKING FOR SOMETHING THAT STANDS OUT.

i HAVE INCLUDED A COPY OF OUR LAST BROCHURE SO YOU CAN SEE THE INFORMATION THAT WE PREVIOUSLY USED AND ALSO OUR PRICING.

WE HAVE MANY DIVE COMPANY'S IN NORTH QUEENSLAND AND THROUGHOUT AUSTRALIA, WE ARE AFTER SOMETHING THAT PEOPLE ARE DRAWN TO AND WILL STAND OUT AMONGST OTHER COMPETITORS.

LOOKING FOR PLAYFUL AND FUN

```html
<!DOCTYPE html>
<html lang="en">
<head>
<meta charset="utf-8">
<title>Brinewake Dive – Courses and Prices</title>
<link href="https://fonts.googleapis.com/css2?family=Arimo:ital,wght@0,400;0,700;1,700&display=swap" rel="stylesheet">
<style>
  :root {
    --backdrop: #8a9ba3;
    --paper: #f7f8f8;
    --ocean-blue: #0aa3e3;
    --ink: #2a2a2a;
    --white: #ffffff;
    --reef-deep: #0b4f9c;
    --reef-mid: #1b7fc4;
    --reef-coral: #8a5a2b;
  }
  * { box-sizing: border-box; margin: 0; padding: 0; }
  html, body { width: 1200px; height: 858px; overflow: hidden; }
  body {
    background: var(--backdrop);
    font-family: "Arimo", Arial, sans-serif;
    color: var(--ink);
    position: relative;
  }
  .brochure {
    position: absolute;
    left: 60px; top: 79px;
    width: 1080px; height: 700px;
    background: var(--paper);
  }
  .brochure-shapes { position: absolute; inset: 0; }
  .panel { position: absolute; top: 0; width: 360px; height: 700px; }
  .panel-about { left: 0; }
  .panel-courses { left: 360px; }
  .panel-prices { left: 720px; }

  .section-title {
    font-weight: 700;
    font-style: italic;
    text-transform: uppercase;
    color: var(--white);
    letter-spacing: 0.5px;
  }
  .panel-about .section-title {
    font-size: 24px;
    text-align: center;
    margin: 34px 0 16px;
  }
  .about-copy {
    color: var(--white);
    font-size: 12.5px;
    line-height: 1.5;
    font-style: italic;
    padding: 0 34px;
  }
  .about-copy p + p { margin-top: 12px; }

  .price-list { list-style: none; font-size: 14.5px; line-height: 1.35; }
  .price-list li { margin-bottom: 12px; }
  .price { color: var(--ocean-blue); font-weight: 700; }
  .panel-courses .price-list { padding: 40px 30px 0 34px; }
  .panel-prices .section-title {
    position: absolute; top: 98px; left: 0; width: 360px;
    text-align: center; font-size: 26px;
  }
  .panel-prices .price-list { padding: 176px 30px 0 34px; }
  .price-note {
    color: var(--ocean-blue);
    font-weight: 700;
    font-size: 15px;
    line-height: 1.3;
    padding: 6px 40px 0 34px;
  }
</style>
</head>
<body>
  <main class="brochure">
    <svg class="brochure-shapes" width="1080" height="700" viewBox="0 0 1080 700">
      <defs>
        <linearGradient id="reef-tones" x1="0" y1="0" x2="0" y2="1">
          <stop offset="0" stop-color="var(--reef-mid)"/>
          <stop offset="0.5" stop-color="var(--reef-deep)"/>
          <stop offset="1" stop-color="var(--reef-coral)"/>
        </linearGradient>
      </defs>
      <rect class="about-band" x="0" y="0" width="360" height="700" fill="var(--ocean-blue)"/>
      <rect class="prices-band" x="720" y="86" width="360" height="62" fill="var(--ocean-blue)"/>
      <path class="reef-photo" role="img" aria-label="Underwater photo of a coral reef with tropical fish, a lionfish and a manta ray"
            d="M20 352 Q190 330 360 358 Q540 400 700 432 Q760 540 850 680 H20 Z"
            fill="url(#reef-tones)" stroke="var(--ocean-blue)" stroke-width="6"/>
    </svg>

    <section class="panel panel-about">
      <h2 class="section-title">About Us</h2>
      <div class="about-copy">
        <p>Brinewake Dive is based on the beautiful Saltmere Island located within 25 minutes from Harrowport, the largest City in far North Queensland. You can find us in the heart of Driftwood Lodge which is in the picturesque Coral Cove. At Brinewake Dive we have our dive pool only steps away from the classroom with stunning views to the ocean and the spectacular Coral Cove.</p>
        <p>We offer a range of courses for beginners through to professional dive qualifications. The dive centre is fully stocked with modern training materials and facilities. We pride ourselves on our calm, safe and laid back teaching environment.</p>
      </div>
    </section>

    <section class="panel panel-courses">
      <ul class="price-list">
        <li>Introductory Discover Scuba Diving <span class="price">$75</span></li>
        <li>Repeat Introductory Discover Scuba Diving <span class="price">$60</span></li>
        <li>Scuba Diver Course <span class="price">$260</span></li>
        <li>Open Water Diver Course (excluding accommodation) <span class="price">$350</span></li>
        <li>Open Water Diver Course (including 4 nights accommodation at Driftwood Lodge) <span class="price">$399</span></li>
        <li>Advanced Open Water Diver Course (including 2 nights accommodation at Driftwood Lodge) <span class="price">$520</span></li>
        <li>Rescue Diver Course <span class="price">$499</span></li>
      </ul>
    </section>

    <section class="panel panel-prices">
      <h2 class="section-title">Courses and Prices</h2>
      <ul class="price-list">
        <li>Divemaster/Dive Control Specialist Course <span class="price">POA</span></li>
        <li>Certified Dive <span class="price">$60</span></li>
        <li>Repeat Certified Dive <span class="price">$40</span></li>
        <li>Refresher Course <span class="price">$95</span></li>
        <li>Night Dive <span class="price">$75</span></li>
        <li>Full Day Diving equipment hire <span class="price">$55</span></li>
        <li>Full Day Snorkel equipment hire <span class="price">$15</span></li>
      </ul>
      <p class="price-note">Prices exclude Reef tax and all courses are subject to a dive medical and weather conditions.</p>
    </section>
  </main>
</body>
</html>
```